Bref créative
Stationary for telecom company
KLV Telecommunications
Professional
Dinh Quoc Bao
Director
47 Hoa Lu Street, Ward 5, Go Vap District, Ho Chi Minh City
bao.dinh@mrq.net.vn
www.klvtelecom.vn

```html
<!DOCTYPE html>
<html lang="en">
<head>
<meta charset="utf-8">
<title>KLV Telecommunications – Business Card</title>
<link href="https://fonts.googleapis.com/css2?family=Open+Sans:wght@400;600;700&display=swap" rel="stylesheet">
<style>
  :root {
    --bg: #e9ebee;
    --card: #ffffff;
    --brand-blue: #1f5a9c;
    --brand-deep: #153f73;
    --brand-light: #7aa4d4;
    --text: #4a4f57;
    --muted: #8a9099;
    --on-blue: #ffffff;
  }
  * { box-sizing: border-box; margin: 0; padding: 0; }
  html, body { width: 1200px; height: 980px; overflow: hidden; }
  body {
    background: var(--bg);
    font-family: "Open Sans", Arial, sans-serif;
    color: var(--text);
    position: relative;
  }
  .card {
    position: absolute;
    left: 220px;
    width: 760px;
    height: 430px;
    background: var(--card);
    border-radius: 28px;
    overflow: hidden;
    box-shadow: 0 6px 18px rgba(0,0,0,0.12);
  }
  .card--back { top: 40px; }
  .card--front { top: 510px; }

  .wordmark {
    display: flex;
    align-items: center;
    gap: 12px;
    color: var(--brand-blue);
    font-weight: 700;
    letter-spacing: 1px;
    text-transform: uppercase;
  }
  .wordmark__dot {
    width: 18px; height: 18px;
    border-radius: 50%;
    background: var(--brand-blue);
    flex: none;
  }

  /* Back side */
  .card--back .wordmark {
    position: absolute;
    top: 150px; left: 0; right: 0;
    justify-content: center;
    font-size: 34px;
  }
  .card--back .website {
    position: absolute;
    top: 228px; left: 0; right: 0;
    text-align: center;
    font-size: 15px;
    letter-spacing: 7px;
    color: var(--muted);
  }

  /* Front side */
  .card--front .wordmark {
    position: absolute;
    top: 46px; left: 48px;
    font-size: 26px;
  }
  .contact-list {
    position: absolute;
    top: 110px; left: 54px;
    list-style: none;
    font-size: 13px;
    line-height: 1.35;
    color: var(--text);
  }
  .contact-list li {
    display: flex;
    align-items: flex-start;
    gap: 10px;
    margin-bottom: 6px;
  }
  .contact-icon {
    width: 16px; height: 16px;
    flex: none;
    margin-top: 1px;
  }
  .wave {
    position: absolute;
    left: 0; bottom: 0;
    width: 760px; height: 430px;
  }
  .signature {
    position: absolute;
    right: 48px; bottom: 36px;
    text-align: right;
    color: var(--on-blue);
  }
  .signature__name { font-size: 20px; font-weight: 600; }
  .signature__role { font-size: 14px; opacity: 0.9; margin-top: 2px; }
</style>
</head>
<body>

<section class="card card--back" aria-label="Card back">
  <div class="wordmark"><span class="wordmark__dot"></span>KLV Telecommunications</div>
  <p class="website">www.klvtelecom.vn</p>
</section>

<section class="card card--front" aria-label="Card front">
  <svg class="wave" viewBox="0 0 760 430" aria-hidden="true">
    <path d="M0 250 C 180 390, 420 380, 760 240 L 760 430 L 0 430 Z" fill="var(--brand-light)" opacity="0.55"/>
    <path d="M0 275 C 200 420, 450 400, 760 265 L 760 430 L 0 430 Z" fill="var(--brand-blue)"/>
    <path d="M0 320 C 220 430, 480 420, 760 300 L 760 430 L 0 430 Z" fill="var(--brand-deep)"/>
    <path d="M0 262 C 190 402, 430 392, 760 252" fill="none" stroke="#ffffff" stroke-width="3"/>
  </svg>

  <div class="wordmark"><span class="wordmark__dot"></span>KLV Telecommunications</div>

  <ul class="contact-list">
    <li>
      <svg class="contact-icon" viewBox="0 0 16 16"><circle cx="8" cy="8" r="8" fill="var(--brand-blue)"/><path d="M8 3.5a2.8 2.8 0 0 0-2.8 2.8C5.2 8.4 8 12 8 12s2.8-3.6 2.8-5.7A2.8 2.8 0 0 0 8 3.5z" fill="#fff"/><circle cx="8" cy="6.3" r="1" fill="var(--brand-blue)"/></svg>
      <span>47 Hoa Lu Street, Ward 5,<br>Go Vap District, Ho Chi Minh City</span>
    </li>
    <li>
      <svg class="contact-icon" viewBox="0 0 16 16"><circle cx="8" cy="8" r="8" fill="var(--brand-blue)"/><path d="M5.2 4h1.6l.8 2-1 .7a5 5 0 0 0 2.7 2.7l.7-1 2 .8v1.6c0 .5-.4.9-.9.9A7.1 7.1 0 0 1 4.3 4.9c0-.5.4-.9.9-.9z" fill="#fff"/></svg>
      <span>(84) 8 39 620417</span>
    </li>
    <li>
      <svg class="contact-icon" viewBox="0 0 16 16"><circle cx="8" cy="8" r="8" fill="var(--brand-blue)"/><rect x="4.5" y="6" width="7" height="4.5" rx="0.6" fill="#fff"/><rect x="5.8" y="3.8" width="4.4" height="2.4" fill="#fff"/></svg>
      <span>(84) 8 39 620455</span>
    </li>
    <li>
      <svg class="contact-icon" viewBox="0 0 16 16"><circle cx="8" cy="8" r="8" fill="var(--brand-blue)"/><rect x="4" y="5" width="8" height="6" rx="0.6" fill="#fff"/><path d="M4.3 5.4 8 8.3l3.7-2.9" fill="none" stroke="var(--brand-blue)" stroke-width="0.9"/></svg>
      <span>bao.dinh@mrq.net.vn</span>
    </li>
    <li>
      <svg class="contact-icon" viewBox="0 0 16 16"><circle cx="8" cy="8" r="8" fill="var(--brand-blue)"/><circle cx="8" cy="8" r="4" fill="none" stroke="#fff" stroke-width="1"/><path d="M4 8h8M8 4c-1.6 2.2-1.6 5.8 0 8M8 4c1.6 2.2 1.6 5.8 0 8" fill="none" stroke="#fff" stroke-width="0.8"/></svg>
      <span>www.klvtelecom.vn</span>
    </li>
  </ul>

  <div class="signature">
    <p class="signature__name">Dinh Quoc Bao</p>
    <p class="signature__role">Director</p>
  </div>
</section>

</body>
</html>
```